Flyer-Design für Linkshänder-Versandhandel
Zielgruppe
Online Versandhandel für Linkshänderprodukte
Aufgabenstellung
- Blau und Grüntöne mit passenden Ergänzungen
- Der Flyer soll ein 6-seitiger Wickelfalz sein
- Innen sollte Platz für Text sein

```html
<!DOCTYPE html>
<html lang="de">
<head>
<meta charset="utf-8">
<title>Tauschwerk – Wickelfalz-Flyer</title>
<link rel="stylesheet" href="https://fonts.googleapis.com/css2?family=Inter:wght@400;500;700;800&display=swap">
<style>
  :root {
    --green: #b3c65d;
    --green-dark: #9fb24a;
    --blue: #3a9fd0;
    --grey-panel: #c9c9c9;
    --grey-light: #e9e9e9;
    --paper: #f7f7f7;
    --ink: #6b6b6b;
    --white: #ffffff;
    --stage: #e4e4e4;
  }
  * { box-sizing: border-box; margin: 0; padding: 0; }
  html, body { width: 1200px; height: 900px; overflow: hidden; }
  body {
    background: var(--stage);
    font-family: "Inter", Arial, sans-serif;
    display: flex;
    align-items: center;
    justify-content: center;
    gap: 28px;
  }
  .spread {
    position: relative;
    display: flex;
    width: 570px;
    height: 412px;
    box-shadow: 0 10px 30px rgba(0,0,0,.12);
    overflow: hidden;
  }
  .panel {
    position: relative;
    width: 190px;
    height: 412px;
    overflow: hidden;
    background: var(--paper);
  }
  .panel + .panel { border-left: 1px solid rgba(0,0,0,.05); }

  .kicker { font-weight: 700; font-size: 9.5px; line-height: 1; letter-spacing: .2px; }
  .headline { font-weight: 800; font-size: 16px; line-height: 1.05; letter-spacing: .2px; }
  .is-green { color: var(--green); }
  .is-blue { color: var(--blue); }
  .is-white { color: var(--white); }
  .copy { font-size: 5.2px; line-height: 1.55; color: var(--ink); }
  .copy.is-white { color: var(--white); }

  .brand { display: flex; align-items: center; gap: 5px; }
  .brand-dot { width: 18px; height: 18px; border-radius: 50%; background: var(--green); flex: none; }
  .brand-name { font-weight: 800; font-size: 11px; color: var(--blue); letter-spacing: .3px; }

  /* Outside: company panel */
  .company .title-block { position: absolute; top: 36px; left: 16px; }
  .company .photo-slot { position: absolute; top: 80px; left: 16px; width: 158px; height: 88px; background: var(--grey-light); }
  .company .about { position: absolute; top: 194px; left: 16px; right: 12px; }
  .company .about h4 { font-size: 5.6px; font-weight: 700; color: var(--green); margin-bottom: 2px; }
  .company .about p + p { margin-top: 7px; }
  .features { position: absolute; top: 318px; left: 16px; right: 12px; display: flex; justify-content: space-between; }
  .feature { text-align: center; width: 44px; }
  .feature-dot { width: 26px; height: 26px; border-radius: 50%; background: var(--green); margin: 0 auto 6px; }
  .feature span { font-size: 5.4px; font-weight: 700; color: var(--green); }

  /* Outside: network panel */
  .network { background: var(--grey-light); }
  .network .top { position: absolute; inset: 0 0 auto 0; height: 100px; background: var(--paper); }
  .network .title-block { position: absolute; top: 32px; left: 16px; }
  .network .info-band { position: absolute; top: 100px; left: 0; width: 190px; height: 268px; background: var(--blue); padding: 24px 16px 0; }
  .network .info-band h3 { font-size: 10px; font-weight: 700; color: var(--white); margin: 50px 0 8px; }
  .network .info-band p + p { margin-top: 9px; }

  /* Outside: cover panel */
  .cover { background: var(--grey-panel); }
  .cover .brand { position: absolute; top: 34px; left: 22px; }
  .cover .hero { position: absolute; top: 100px; left: 0; width: 190px; height: 272px; background: var(--green); }
  .cover .hero-text { position: absolute; top: 118px; left: 16px; z-index: 2; }
  .cover .hero-text .kicker { font-size: 13px; margin-bottom: 3px; }
  .cover .hero-text .headline { font-size: 27px; line-height: .95; }
  .hand-art {
    position: absolute; left: 26px; top: 190px; width: 150px; height: 230px;
    border-radius: 60px 60px 20px 20px;
    background: linear-gradient(180deg, #e4e4e4, #bdbdbd);
    opacity: .9;
  }

  /* Inside: quote panel */
  .quote { background: linear-gradient(180deg, #d4d4d4, #c3c3c3); }
  .quote .disc { position: absolute; left: -86px; top: 64px; width: 258px; height: 258px; border-radius: 50%; background: var(--green); }
  .quote .statement { position: absolute; top: 94px; left: 18px; z-index: 3; font-weight: 800; font-size: 22px; line-height: .98; color: var(--white); }
  .quote .signature { position: absolute; top: 228px; left: 14px; width: 90px; height: 10px; border-radius: 5px; background: rgba(255,255,255,.35); z-index: 3; }
  .quote .caption { position: absolute; top: 244px; left: 18px; font-size: 4.6px; font-weight: 700; color: var(--white); z-index: 3; }
  .quote .brand { position: absolute; bottom: 38px; left: 18px; z-index: 3; }

  .portrait-art {
    position: absolute; left: 132px; top: 104px; width: 98px; height: 288px; z-index: 2;
    border-radius: 50px 50px 10px 30px;
    background: linear-gradient(160deg, rgba(235,235,235,.9), rgba(140,140,140,.7));
  }

  /* Inside: offer panel */
  .offer { background: linear-gradient(180deg, var(--paper) 0%, #ececec 100%); }
  .offer .title-block { position: absolute; top: 66px; left: 18px; }
  .offer .body { position: absolute; top: 108px; left: 46px; right: 16px; text-align: right; }
  .offer .body p + p { margin-top: 7px; }
  .offer .body .more { font-size: 5.4px; font-weight: 700; color: var(--blue); margin-top: 8px; }
  .offer .deal { position: absolute; left: 58px; top: 275px; width: 118px; height: 108px; background: var(--green); padding: 12px 9px; }
  .offer .deal h3 { font-size: 9.5px; font-weight: 700; line-height: 1; color: var(--white); }
  .offer .deal p { position: absolute; bottom: 8px; left: 9px; right: 9px; }
  .offer .price { position: absolute; left: 148px; top: 252px; width: 36px; height: 36px; border-radius: 50%; background: var(--blue); color: var(--white); font-weight: 700; font-size: 8px; display: flex; align-items: center; justify-content: center; z-index: 2; }

  /* Inside: famous people panel */
  .famous { background: var(--paper); }
  .famous .title-block { position: absolute; top: 60px; left: 18px; }
  .people { position: absolute; top: 106px; left: 14px; right: 10px; list-style: none; }
  .person { display: flex; align-items: center; gap: 12px; height: 51px; }
  .person-photo { position: relative; width: 38px; height: 38px; flex: none; }
  .person-photo::before { content: ""; position: absolute; inset: 0 3px 0 -3px; border-radius: 50%; background: var(--blue); }
  .person-photo .tone { position: absolute; inset: 0; border-radius: 50%; background: radial-gradient(circle at 50% 40%, #9a9a9a, #3c3c3c); }
  .person-photo.ring-green::before { background: var(--green); }
  .person h4 { font-size: 5.3px; font-weight: 700; color: var(--green); margin-bottom: 1px; }
</style>
</head>
<body>

<!-- Outside of the roll fold -->
<section class="spread outside">
  <article class="panel company">
    <div class="title-block">
      <p class="kicker is-green">DAS MACHEN WIR</p>
      <p class="headline is-green">MIT LINKS.</p>
    </div>
    <div class="photo-slot" role="img" aria-label="Platz für ein Unternehmensfoto"></div>
    <div class="about copy">
      <h4>UNSER UNTERNEHMEN</h4>
      <p>fugia dem quam, es ut veri ni blaut es aut aliquibus am id quas apiet et aliam que conserum volorem exeribus rehendi tatempel ium volorehent. Lique dolum aliquate num rehenisti velende bisqui que conserum volorem exeribus rehendi tatempel ium volorehent. Lique dolum aliquate num rehenisti velende bisqui que conserum</p>
      <p>volorem exeribus rehendi tatempel ium volorehent. Lique dolum aliquate num rehenisti velend aliquate num rehenisti velende bisqui que conserum volorem exeribus re</p>
    </div>
    <div class="features">
      <div class="feature"><div class="feature-dot"></div><span>VIDENDIT</span></div>
      <div class="feature"><div class="feature-dot"></div><span>VIDENDIT</span></div>
      <div class="feature"><div class="feature-dot"></div><span>VIDENDIT</span></div>
    </div>
  </article>

  <article class="panel network">
    <div class="top"></div>
    <div class="title-block">
      <p class="kicker is-blue">WIR SIND AUCH</p>
      <p class="headline is-blue">VER(LINK)T.</p>
    </div>
    <div class="info-band">
      <p class="copy is-white">Ga. Ut la sum ni cum videndit fugia dem quam, es ut veri ni blaut es aut aliquibus am id quas apiet et aliam que conserum volorem exeribus rehendi tatempel ium volorehent. Lique dolum aliquate num rehenisti velende bisqui</p>
      <h3>KONTAKT</h3>
      <p class="copy is-white">Ga. Ut la sum ni cum videndit fugia dem quam, es ut veri ni blaut es aut aliquibus am id quas apiet et aliam que conserum volorem exe</p>
      <p class="copy is-white">Ga. Ut la sum ni cum videndit fugia dem quam, es ut veri ni blaut es aut aliquibus am id quas apiet et aliam que conserum volorem exe</p>
    </div>
  </article>

  <article class="panel cover">
    <div class="brand"><span class="brand-dot"></span><span class="brand-name">TAUSCHWERK</span></div>
    <div class="hero"></div>
    <div class="hand-art" role="img" aria-label="Illustration einer zeigenden linken Hand"></div>
    <div class="hero-text">
      <p class="kicker is-white">MACHEN SIE</p>
      <p class="headline is-white">ALLES MIT<br>LINKS?</p>
    </div>
  </article>
</section>

<!-- Inside of the roll fold -->
<section class="spread inside">
  <article class="panel quote">
    <div class="disc"></div>
    <p class="statement">LINKS<br>IST<br>MEINE<br>SCHOKO<br>LADEN<br>SEITE</p>
    <div class="signature" role="img" aria-label="Handschriftliche Signatur von Marlene Rowe"></div>
    <p class="caption">Berühmte Linkshänderin</p>
    <div class="brand"><span class="brand-dot"></span><span class="brand-name">TAUSCHWERK</span></div>
  </article>

  <article class="panel offer">
    <div class="title-block">
      <p class="kicker is-blue">DAS KAUFE ICH</p>
      <p class="headline is-blue">MIT LINKS.</p>
    </div>
    <div class="body copy">
      <p>Ga. Ut la sum ni cum videndit fugia dem quam, es ut veri ni blaut es aut aliquibus am id quas apiet et aliam que conserum volorem exeribus rehendi tatempel ium volorehent. Lique dolum aliquate num rehenisti velende bisqui Ga.</p>
      <p>Ut la sum ni cum videndit fugia dem quam, es ut veri ni blaut es aut aliquibus am id quas apiet et aliam que conserum volorem exeribus rehendi tatempel ium volorehent. Lique dolum aliquate num</p>
      <p class="more">REHENISTI VELENDE BISQUI</p>
    </div>
    <div class="price">€ XX.-</div>
    <div class="deal">
      <h3>ANGEBOT<br>DES MONATS</h3>
      <p class="copy is-white">videndit fugia dem quam, es ut veri et aliam que conserum volorem exeribus rehendi</p>
    </div>
  </article>

  <article class="panel famous">
    <div class="title-block">
      <p class="kicker is-green">BERÜHMTE</p>
      <p class="headline is-green">LINKSHÄNDER.</p>
    </div>
    <ul class="people">
      <li class="person">
        <div class="person-photo" role="img" aria-label="Porträt von Gaius Aurelius Varro"><div class="tone"></div></div>
        <div><h4>GAIUS AURELIUS VARRO</h4><p class="copy">ni cum videndit fugia dem quam, es ut veri et aliam que conserum bisqui</p></div>
      </li>
      <li class="person">
        <div class="person-photo ring-green" role="img" aria-label="Porträt von Lorenzo Bellandi"><div class="tone"></div></div>
        <div><h4>LORENZO BELLANDI</h4><p class="copy">dem quam, es ut veri et aliam que conserum volorem exeribus rehendi tatempel</p></div>
      </li>
      <li class="person">
        <div class="person-photo" role="img" aria-label="Porträt von Ludwig Albrecht Kessler"><div class="tone"></div></div>
        <div><h4>LUDWIG ALBRECHT KESSLER</h4><p class="copy">cum videndit fugia dem quam, es ut veri et aliam que conserum volorem exeribus rehendi tatempel ium</p></div>
      </li>
      <li class="person">
        <div class="person-photo ring-green" role="img" aria-label="Porträt von Marlene Rowe"><div class="tone"></div></div>
        <div><h4>MARLENE ROWE</h4><p class="copy">videndit fugia dem quam, es ut veri et aliam que conserum volorem exeribus rehendi tatempel ium volorehent.</p></div>
      </li>
      <li class="person">
        <div class="person-photo" role="img" aria-label="Porträt von Jimmy Harlow"><div class="tone"></div></div>
        <div><h4>JIMMY HARLOW</h4><p class="copy">cum videndit fugia dem quam, es ut veri et aliam que conserum volorem exeribus rehendqui</p></div>
      </li>
    </ul>
  </article>

  <div class="portrait-art" role="img" aria-label="Grafische Illustration von Marlene Rowe in Grautönen"></div>
</section>

</body>
</html>
```